Looking for a high-end business card design for a construction company

We are looking to update our business card design. We are a post-frame construction company that builds custom buildings, commercial spaces, homes, and anything else. We have multiple people working here so we would need something we can easily customize the information for the specific person. We need a name, website, cell phone, office phone as well as social icons. Our colors are black, white, and grey/silver so I would love a black background or something that is more striking than just a traditional white business card. Looking for something that is very professional with a high-end look/feel. I have attached our logos, they can be silver, white, grey, or black.
Industry/Entity Type
Construction
Contact Information for Business Card
Business logo, Name, Cell phone, Office phone, website, social Icons
Colors
Designer to choose only greyscale colors for use in the design.
Look and feel

```html
<!DOCTYPE html>
<html lang="en">
<head>
<meta charset="utf-8">
<title>Korvath Builders, Inc. — Business Card</title>
<link href="https://fonts.googleapis.com/css2?family=Arimo:wght@400;700&display=swap" rel="stylesheet">
<style>
  :root {
    --stage: #1c1c1c;
    --card: #0b0b0b;
    --card-edge: #222222;
    --white: #ffffff;
    --silver: #c9c9c9;
    --grey: #8a8a8a;
    --rule: #3a3a3a;
  }
  * { box-sizing: border-box; margin: 0; padding: 0; }
  html, body {
    width: 1200px;
    height: 900px;
    overflow: hidden;
    background: var(--stage);
    font-family: "Arimo", Arial, sans-serif;
  }
  .stage {
    position: relative;
    width: 1200px;
    height: 900px;
  }
  .card {
    position: absolute;
    width: 560px;
    height: 320px;
    background: var(--card);
    border-radius: 22px;
    box-shadow: 0 18px 40px rgba(0, 0, 0, 0.55), 0 0 0 1px var(--card-edge);
    overflow: hidden;
  }

  /* Front: contact side */
  .card--front {
    left: 60px;
    top: 500px;
    display: flex;
  }
  .card--front .brand-panel {
    width: 270px;
    display: flex;
    align-items: center;
    justify-content: center;
  }
  .card--front .divider {
    width: 1px;
    background: var(--rule);
  }
  .brand-name {
    color: var(--white);
    font-weight: 700;
    text-transform: uppercase;
    text-align: center;
    line-height: 1.05;
    letter-spacing: 2px;
  }
  .brand-name .line-1 { display: block; font-size: 34px; }
  .brand-name .line-2 { display: block; font-size: 17px; letter-spacing: 3px; }

  .contact-panel {
    flex: 1;
    padding: 48px 0 0 34px;
    color: var(--white);
  }
  .person-name {
    font-size: 24px;
    font-weight: 700;
    letter-spacing: 1px;
    text-transform: uppercase;
  }
  .person-role {
    font-size: 16px;
    margin-top: 2px;
  }
  .contact-list {
    list-style: none;
    margin-top: 30px;
  }
  .contact-list li {
    display: flex;
    align-items: center;
    gap: 8px;
    font-size: 17px;
    line-height: 25px;
    white-space: nowrap;
  }
  .contact-list svg {
    width: 16px;
    height: 16px;
    flex: none;
  }

  /* Back: brand side */
  .card--back {
    left: 580px;
    top: 90px;
    display: flex;
    flex-direction: column;
    align-items: center;
    justify-content: center;
  }
  .card--back .brand-name { color: var(--silver); }
  .card--back .brand-name .line-1 { font-size: 46px; }
  .card--back .brand-name .line-2 { font-size: 22px; letter-spacing: 4px; }
  .social-row {
    display: flex;
    align-items: center;
    gap: 10px;
    margin-top: 34px;
  }
  .social-row .rule {
    width: 120px;
    height: 1px;
    background: var(--grey);
  }
  .social-row .dot {
    width: 20px;
    height: 20px;
    border-radius: 50%;
    background: var(--grey);
  }
</style>
</head>
<body>
<main class="stage">

  <section class="card card--front" aria-label="Business card front">
    <div class="brand-panel">
      <p class="brand-name"><span class="line-1">Korvath</span><span class="line-2">Builders, Inc.</span></p>
    </div>
    <div class="divider"></div>
    <div class="contact-panel">
      <h1 class="person-name">Marcus Hale</h1>
      <p class="person-role">Managing Director</p>
      <ul class="contact-list">
        <li>
          <svg viewBox="0 0 16 16" aria-hidden="true"><path d="M4 1.5l2.2 3-1.4 1.6c.9 2 2.6 3.7 4.6 4.6l1.6-1.4 3 2.2-1.2 2.5C7.5 13.8 2.2 8.5 1.5 2.7z" fill="var(--white)"/></svg>
          <span>044-555 210 430</span>
        </li>
        <li>
          <svg viewBox="0 0 16 16" aria-hidden="true"><rect x="4" y="1" width="8" height="14" rx="1.5" fill="none" stroke="var(--white)" stroke-width="1.5"/><circle cx="8" cy="12.5" r="0.9" fill="var(--white)"/></svg>
          <span>044-555 210 431</span>
        </li>
        <li>
          <svg viewBox="0 0 16 16" aria-hidden="true"><rect x="1" y="3" width="14" height="10" fill="var(--white)"/><path d="M1 3l7 6 7-6" fill="none" stroke="var(--card)" stroke-width="1.3"/></svg>
          <span>info@korvath.com</span>
        </li>
        <li>
          <svg viewBox="0 0 16 16" aria-hidden="true"><g fill="none" stroke="var(--white)" stroke-width="1.2"><circle cx="8" cy="8" r="6.5"/><ellipse cx="8" cy="8" rx="3" ry="6.5"/><path d="M1.5 8h13M2.5 4.5h11M2.5 11.5h11"/></g></svg>
          <span>www.korvathbuild.com</span>
        </li>
      </ul>
    </div>
  </section>

  <section class="card card--back" aria-label="Business card back">
    <p class="brand-name"><span class="line-1">Korvath</span><span class="line-2">Builders, Inc.</span></p>
    <div class="social-row" aria-label="Social media links">
      <span class="rule"></span>
      <span class="dot"></span>
      <span class="dot"></span>
      <span class="dot"></span>
      <span class="rule"></span>
    </div>
  </section>

</main>
</body>
</html>
```